Lantern Square, Steady Course. (Website Design)

We are launching a new bipartisan civic movement: Lantern Square. Steady Course.
The mission is this: Americans deserve a government that is legally required to serve them honestly.
We are looking for a world-class website designer capable of creating an emotionally powerful, modern, cinematic landing page experience that feels larger than politics.
This is not a campaign website for a political party or candidate. We are not looking for a red, white, and blue page with stripes, or American flags, or stock footage of smiling people in a voting booth. We are looking for an emotional and cinematic experience through and through.
The visual direction should feel:
Historic
Hopeful
American
Emotional
Cinematic
Trustworthy
Timeless
The goal is to make visitors feel that they are witnessing the beginning of something important and want to be part of it in the end.
Primary Objective:
Inspire visitors to participate in a one-minute survey and cast their vote.
The survey itself is extremely short and takes approximately one minute to complete.
Everything on the page should ultimately guide visitors toward this action while creating enough curiosity, trust, emotional engagement, and excitement that they feel compelled to take part in the movement.
Audience:
The audience is ordinary Americans across the political spectrum: Democrats, Republicans, Independents.
The design should feel unifying and welcoming.
It should avoid looking partisan, ideological, activist, or government-issued.
Creative Freedom:
We are intentionally giving designers substantial creative freedom.
We are not looking for someone to simply arrange content into predefined sections.
Instead, we are looking for a designer who can think strategically about user experience and persuasion.
The ideal design is as minimal as possible, but you may always:
Use as many sections as you believe are necessary.
Use as many images as you believe are necessary.
Include storytelling elements.
Include data visualizations.
Include timelines.
Include videos.
Include animations.
Include or exclude sections as you see fit.
Reorganize the flow entirely.
We uploaded some files containing text and section suggestions. You don’t have to use them.
We also uploaded some images to convey the general feel we’re looking for.
We are much more interested in the effectiveness of the overall experience than in any specific layout.
What success looks like:
Think outside the box.
Please do not create another generic political website. We have already explored those approaches.
We are looking for something different.
The winning design will be the one that most effectively guides visitors from curiosity to belief to participation.
When a visitor reaches the end of the experience, they should feel:
This is bigger than politics.
This is something I can support regardless of party.
This feels credible.
This feels hopeful.
I want to be part of this.
Use the survey results, the research findings, the principles, the storytelling, or any other elements you believe will help build trust and inspire participation.
Don't just impress us with flashy visuals. Impress us with a website experience that inspires people to become part of the movement and cast their vote.
The final call-to-action should feel like the natural conclusion of the journey, not a request for engagement.
Our goal is not simply to inform visitors. Our goal is to inspire them to cast their vote.
Prioritize emotional impact, storytelling, clarity, and persuasion over decorative design elements.
Final words:
Design a website experience that successfully inspires visitors to take the survey and cast their vote.
Think like a storyteller, not just a designer.
Thank you for your interest in the project.
Best of luck.

```html
<!DOCTYPE html>
<html lang="en">
<head>
<meta charset="utf-8">
<title>Lantern Square. Steady Course.</title>
<link rel="stylesheet" href="https://fonts.googleapis.com/css2?family=Montserrat:ital,wght@0,500;0,600;0,700;1,700&family=Inter:wght@400;500&family=Tinos&family=Cormorant+Garamond:wght@500&display=swap">
<style>
:root{
  --navy:#1b2130;
  --navy-deep:#161b27;
  --gold:#c8974e;
  --gold-card:#c99a52;
  --white:#ffffff;
  --ink:#15171c;
  --muted:#6b6f78;
  --mist:#e9e8ee;
}
*{box-sizing:border-box;margin:0;padding:0}
html,body{width:1200px;height:4121px;overflow:hidden}
body{font-family:"Inter",sans-serif;color:var(--ink);background:var(--white);position:relative}
section,header,footer{position:relative;width:1200px}

.site-nav{height:88px;background:var(--navy);display:flex;align-items:center;justify-content:space-between;padding:0 90px}
.site-nav .brand{font-family:"Montserrat",sans-serif;font-weight:700;font-size:24px;color:var(--white)}
.site-nav ul{display:flex;gap:48px;list-style:none;margin-right:0}
.site-nav li{font-family:"Montserrat",sans-serif;font-weight:500;font-size:11px;color:var(--white);letter-spacing:.3px}

.hero{height:626px;overflow:hidden}
.hero-photo{position:absolute;inset:0;background:
  radial-gradient(ellipse at 78% 45%,rgba(255,200,120,.85) 0%,rgba(214,140,70,.55) 22%,transparent 50%),
  linear-gradient(100deg,#3b2e22 0%,#6b5238 30%,#8a6a48 55%,#6c4f36 80%,#3c2c1f 100%)}
.hero-copy{position:absolute;left:144px;top:440px}
.hero-title{font-family:"Montserrat",sans-serif;font-weight:700;font-size:72px;line-height:.96;letter-spacing:-.5px}
.hero-title .line-one{color:var(--white);display:block}
.hero-title .line-two{color:var(--gold);display:block}
.hero-sub{margin-top:22px;font-size:16px;color:var(--white)}

.problem{height:513px;display:flex}
.problem-copy{width:600px;padding:118px 40px 0 59px}
.problem-copy h2{font-family:"Montserrat",sans-serif;font-weight:700;font-size:34px;line-height:1.2}
.problem-copy p{margin-top:16px;font-size:19px;line-height:1.45}
.problem-copy .lead-in{margin-top:30px;font-size:15px;color:var(--gold);letter-spacing:.3px}
.problem-photo{width:600px;height:513px;background:linear-gradient(160deg,#6a5a4c 0%,#4a3f37 45%,#2f2a28 100%)}

.about{height:285px;text-align:center;padding-top:60px}
.about h2{font-family:"Montserrat",sans-serif;font-weight:700;font-size:34px;line-height:1.2;width:600px;margin:0 auto}
.about p{width:680px;margin:24px auto 0;font-size:14px;line-height:1.6}
.about p + p{margin-top:22px}

.memory-strip{height:280px;background:var(--mist);overflow:hidden}
.memory-strip .band{position:absolute;inset:0;background:var(--navy-deep);clip-path:polygon(0 16%,100% 6%,100% 100%,0 100%)}
.memory-strip .frame{position:absolute;bottom:0}
.frame-one{left:0;width:315px;height:220px;background:linear-gradient(135deg,#6f8aa6,#c8a486 60%,#7a5c48)}
.frame-two{left:347px;width:503px;height:232px;background:linear-gradient(180deg,#d9d2c4 0%,#8f8a84 45%,#2a2a2c 100%)}
.frame-three{left:880px;width:320px;height:245px;background:linear-gradient(135deg,#b59a80,#8a6f58 50%,#c2a88d)}

.journey{height:701px;background:var(--navy);color:var(--white)}
.journey h2{font-family:"Tinos",serif;font-weight:400;font-size:38px;text-align:center;padding-top:72px}
.timeline-axis{position:absolute;left:599px;top:195px;width:1px;height:405px;background:#3a4254}
.timeline-node{position:absolute;left:590px;width:20px;height:20px;border:1.5px solid var(--gold);border-radius:50%;background:var(--navy)}
.milestone{position:absolute;width:420px}
.milestone.right{left:656px;text-align:left}
.milestone.left{left:127px;text-align:right}
.milestone .month{font-size:13px;color:var(--gold);letter-spacing:.5px}
.milestone .year{font-family:"Montserrat",sans-serif;font-weight:500;font-size:36px;color:var(--gold);line-height:1.05}
.milestone p{font-size:13.5px;line-height:1.5;margin-top:4px}

.principles{height:1003px}
.principles h2{font-family:"Montserrat",sans-serif;font-weight:700;font-size:34px;line-height:1.2;text-align:center;padding-top:96px}
.principle{position:absolute;width:445px;height:157px;border-radius:10px;padding:0 28px 0 48px;display:flex;align-items:center;box-shadow:0 10px 22px rgba(0,0,0,.12);overflow:hidden}
.principle.dark{background:var(--navy);color:var(--white)}
.principle.gold{background:var(--gold-card);color:var(--white)}
.principle .num{position:absolute;left:46px;top:12px;font-family:"Montserrat",sans-serif;font-weight:700;font-size:76px;line-height:1}
.principle.dark .num{color:rgba(255,255,255,.14)}
.principle.gold .num{color:rgba(0,0,0,.12)}
.principle p{position:relative;font-size:15.5px;line-height:1.55;margin-top:10px}
.stat{position:absolute;left:613px;top:763px;width:443px;text-align:center}
.stat .figure{font-family:"Montserrat",sans-serif;font-weight:700;font-size:70px;color:var(--gold);line-height:1}
.stat .label{font-size:14px;color:var(--gold);letter-spacing:1px;margin-top:4px}

.call{height:424px;background:linear-gradient(90deg,#b98a48 0%,#cd9d58 40%,#c79650 70%,#b88947 100%);text-align:center;color:var(--white)}
.call-photo{position:absolute;inset:0}
.call h2{position:relative;font-family:"Montserrat",sans-serif;font-weight:700;font-size:32px;line-height:1.25;padding-top:66px;width:700px;margin:0 auto}
.call .bridge{position:relative;font-size:13.5px;margin-top:14px}
.call .promise{position:relative;font-family:"Montserrat",sans-serif;font-style:italic;font-weight:700;font-size:26px;line-height:1.15;margin:18px auto 0;width:600px}
.call .close{position:relative;font-size:13.5px;margin-top:18px}
.call .vote-button{position:absolute;left:485px;top:310px;width:229px;height:40px;background:var(--navy);border-radius:5px;color:var(--white);font-size:12px;display:flex;align-items:center;justify-content:center}

.site-footer{height:201px;text-align:center;padding-top:56px}
.site-footer .brand{font-family:"Cormorant Garamond",serif;font-weight:500;font-size:24px;color:#3b3e45}
.site-footer .brand span{color:var(--gold)}
.site-footer ul{list-style:none;display:flex;justify-content:center;gap:52px;margin-top:14px}
.site-footer li{font-family:"Montserrat",sans-serif;font-weight:500;font-size:11px;color:var(--ink)}
.site-footer .legal{font-size:11px;color:var(--muted);margin-top:18px}
</style>
</head>
<body>

<header class="site-nav">
  <div class="brand">Lantern Square. Steady Course.</div>
  <ul>
    <li>MISSION</li><li>WHO WE ARE</li><li>OUR JOURNEY</li><li>PRINCIPLES</li><li>VOTE</li>
  </ul>
</header>

<section class="hero">
  <div class="hero-photo" role="img" aria-label="Warm sunset scene with a monument statue and a person holding a waving flag"></div>
  <div class="hero-copy">
    <h1 class="hero-title"><span class="line-one">Lantern Square.</span><span class="line-two">Steady Course.</span></h1>
    <p class="hero-sub">Americans deserve a government that is legally required to serve them honestly.</p>
  </div>
</section>

<section class="problem">
  <div class="problem-copy">
    <h2>Today, not a single law binds our government to act honestly, and in our best interest.</h2>
    <p>If our government exists solely to serve us,<br>why isn't it legally required to?</p>
    <p class="lead-in">WE FOUNDED THIS MOVEMENT TO CHANGE THAT.</p>
  </div>
  <div class="problem-photo" role="img" aria-label="Faded historic portrait blended with a waving flag above a stone monument"></div>
</section>

<section class="about">
  <h2>A bipartisan movement based in Washington, D.C.</h2>
  <p>We believe Americans deserve a government legally required to act honestly, transparently, and in the public's best interest.</p>
  <p>At a time of growing division and distrust, we are working to unite Americans around a simple idea: government should faithfully serve the people, not special interests.</p>
</section>

<section class="memory-strip">
  <div class="band"></div>
  <div class="frame frame-one" role="img" aria-label="Historic photograph of a leader speaking"></div>
  <div class="frame frame-two" role="img" aria-label="Historic civil rights march with marchers holding placards"></div>
  <div class="frame frame-three" role="img" aria-label="Bootprint pressed into lunar soil"></div>
</section>

<section class="journey">
  <h2>From an idea, to a movement, to a vote.</h2>
  <div class="timeline-axis"></div>
  <div class="timeline-node" style="top:1977px;top:185px"></div>
  <div class="timeline-node" style="top:297px"></div>
  <div class="timeline-node" style="top:406px"></div>
  <div class="timeline-node" style="top:515px"></div>

  <div class="milestone right" style="top:180px">
    <div class="month">AUGUST</div><div class="year">2024</div>
    <p>We started a nonprofit with this goal in mind:<br>Americans deserve an honest government.</p>
  </div>
  <div class="milestone left" style="top:292px">
    <div class="month">OCTOBER</div><div class="year">2025</div>
    <p>We identified 10 principles that most Americans<br>agree our government must uphold.</p>
  </div>
  <div class="milestone right" style="top:400px">
    <div class="month">MARCH</div><div class="year">2026</div>
    <p>We turned those principles into a rigorous framework<br>and named it Lantern Square, Steady Course.</p>
  </div>
  <div class="milestone left" style="top:503px">
    <div class="month">APRIL</div><div class="year">2026</div>
    <p>We tested the framework in a pre-registered national<br>study with Americans across the political spectrum.</p>
  </div>
</section>

<section class="principles">
  <h2>Seven ideas almost every American<br>agrees on.</h2>

  <div class="principle dark" style="left:142px;top:240px"><span class="num">01</span><p>Public officials should only serve the public good. Not private interests.</p></div>
  <div class="principle gold" style="left:613px;top:240px"><span class="num">02</span><p>Major government decisions should be based on truth and rigorous evidence. Not party loyalty, pressure, or donors.</p></div>
  <div class="principle gold" style="left:142px;top:408px"><span class="num">03</span><p>When a public decision is made, people should be able to see the reasoning. Clearly. Honestly. On the record.</p></div>
  <div class="principle dark" style="left:613px;top:408px"><span class="num">04</span><p>And if the government's reasoning is flawed, citizens should have a way to challenge it, and get a real response.</p></div>
  <div class="principle dark" style="left:142px;top:581px"><span class="num">05</span><p>Conflicts of interest in public office should all be disclosed, before decisions are made.</p></div>
  <div class="principle gold" style="left:613px;top:581px"><span class="num">06</span><p>Lying or misleading the public in official decisions should carry consequences. Real ones.</p></div>
  <div class="principle gold" style="left:142px;top:750px"><span class="num">07</span><p>And most importantly — money should never outweigh people's voice.</p></div>

  <div class="stat">
    <div class="figure">89.9%</div>
    <div class="label">OF AMERICANS AGREED</div>
  </div>
</section>

<section class="call">
  <div class="call-photo" role="img" aria-label="Gold-toned historic scene of a capitol dome and a crowd of marchers with banners" style="background:radial-gradient(ellipse at 15% 50%,rgba(255,255,255,.12),transparent 40%),radial-gradient(ellipse at 85% 55%,rgba(120,80,30,.18),transparent 45%)"></div>
  <h2>For decades, we have argued over policies, parties, and ideologies.</h2>
  <p class="bridge">But today, across political lines, generations, and races, Americans are arriving at the same conclusion:</p>
  <p class="promise">We deserve a government legally required to serve the people honestly.</p>
  <p class="close">And we don't have to ask for it. We just have to vote for it.</p>
  <div class="vote-button">Be Part of History. Vote Now.</div>
</section>

<footer class="site-footer">
  <div class="brand">Lantern Square. <span>Steady Course.</span></div>
  <ul>
    <li>MISSION</li><li>WHO WE ARE</li><li>OUR JOURNEY</li><li>PRINCIPLES</li><li>VOTE</li>
  </ul>
  <p class="legal">© Copyright 2026 | All Right Reserved</p>
</footer>

</body>
</html>
```